Healthcare Seminar Flyer

We will be holding a Healthcare (HIPAA) and Cybersecurity seminar, and would like a flyer to hand out to potential participants.

Target Market(s)

Healthcare

Colors
0054AA
0677BA
7BADD7
CADEEF
E8F1F8

Requirements
Must have
• See attached word document

```html
<!DOCTYPE html>
<html lang="en">
<head>
<meta charset="utf-8">
<title>HIPAA Compliance Officer Course Flyer</title>
<link href="https://fonts.googleapis.com/css2?family=Montserrat:wght@800&family=Rubik:wght@400;500;600;700&family=Roboto:ital,wght@0,400;0,500;0,700;1,400;1,500&display=swap" rel="stylesheet">
<style>
  :root {
    --navy: #1b2a4a;
    --ink: #111111;
    --brand-blue: #0054AA;
    --mid-blue: #0677BA;
    --sky: #7BADD7;
    --mist: #CADEEF;
    --pale: #E8F1F8;
    --band: #1255A8;
    --white: #ffffff;
  }
  * { margin: 0; padding: 0; box-sizing: border-box; }
  html, body { width: 927px; height: 1200px; overflow: hidden; }
  body { font-family: 'Roboto', sans-serif; color: var(--ink); background: var(--white); }
  .flyer { position: relative; width: 927px; height: 1200px; overflow: hidden; background: var(--pale); }
  .hero { position: absolute; left: 0; top: 0; width: 927px; height: 340px; background: linear-gradient(180deg, #f3f6f9 0%, #fafbfd 100%); }

  .title { position: absolute; left: 62px; top: 44px; font-family: 'Montserrat', sans-serif; font-weight: 800; font-size: 41px; line-height: 47px; color: var(--ink); }
  .title .accent { color: var(--brand-blue); }

  .event-date { position: absolute; right: 35px; top: 48px; text-align: right; font-family: 'Rubik', sans-serif; font-weight: 600; font-size: 24px; color: var(--navy); }
  .event-date .lunch { display: block; font-family: 'Roboto', sans-serif; font-style: italic; font-weight: 500; font-size: 20px; color: var(--brand-blue); margin-top: 2px; margin-right: 5px; }
  .venue { position: absolute; left: 552px; top: 131px; font-family: 'Roboto', sans-serif; font-size: 16.5px; line-height: 21px; color: #222; }

  .photo-frame { position: absolute; left: 47px; top: 217px; width: 340px; height: 250px; }

  .price { position: absolute; right: 35px; top: 259px; text-align: right; font-family: 'Rubik', sans-serif; font-weight: 600; font-size: 27px; line-height: 31px; color: var(--ink); }
  .register-label { position: absolute; right: 35px; top: 360px; font-family: 'Rubik', sans-serif; font-weight: 700; font-size: 26px; color: var(--brand-blue); }
  .register-url { position: absolute; right: 35px; top: 394px; font-family: 'Roboto', sans-serif; font-size: 27px; color: var(--navy); }

  .session { position: absolute; left: 42px; width: 860px; }
  .session-label { position: absolute; left: 0; top: 0; width: 205px; }
  .session-title { display: inline-block; background: linear-gradient(90deg, var(--white) 75%, rgba(255,255,255,0)); padding: 2px 60px 2px 8px; font-family: 'Rubik', sans-serif; font-weight: 500; font-size: 19px; color: var(--ink); white-space: nowrap; }
  .presented { margin: 4px 0 0 8px; font-size: 11px; letter-spacing: 1.6px; color: #222; }
  .presenter { margin: 1px 0 0 8px; font-weight: 700; font-size: 15.5px; letter-spacing: 1.3px; color: var(--ink); }
  .partner-mark { display: flex; align-items: center; gap: 6px; margin: 10px 0 0 8px; font-family: 'Roboto', sans-serif; font-weight: 700; font-size: 13px; color: var(--navy); }
  .partner-mark .dot { width: 12px; height: 12px; background: var(--mid-blue); }
  .partner-name { margin: 5px 0 0 7px; font-weight: 700; font-size: 12px; letter-spacing: 1px; color: var(--ink); }

  .topics { position: absolute; top: 0; width: 270px; list-style: none; font-size: 13px; line-height: 16.5px; color: #111; }
  .topics li { position: relative; padding-left: 19px; margin-bottom: 8px; }
  .topics li::before { content: ""; position: absolute; left: 3px; top: 5px; width: 6px; height: 6px; border-radius: 50%; background: var(--ink); }
  .topics.col-a { left: 254px; top: -1px; }
  .topics.col-b { left: 568px; }

  .kit-band { position: absolute; left: 0; top: 942px; width: 927px; height: 258px; background: var(--band); color: var(--white); text-align: center; }
  .kit-title { margin-top: 30px; font-family: 'Roboto', sans-serif; font-weight: 700; font-size: 30px; }
  .kit-sub { margin-top: 5px; font-style: italic; font-size: 15px; }
  .kit-items { position: absolute; left: 0; top: 110px; width: 927px; }
  .kit-item { position: absolute; width: 200px; text-align: center; font-style: italic; font-weight: 500; font-size: 13px; line-height: 16.5px; }
  .kit-item svg { display: block; margin: 0 auto 14px; }
  .badge { position: absolute; left: 776px; top: 902px; width: 92px; height: 92px; border-radius: 50%; background: var(--white); display: flex; align-items: center; justify-content: center; text-align: center; font-style: italic; font-size: 13px; line-height: 16px; color: var(--navy); }
</style>
</head>
<body>
<div class="flyer">
  <div class="hero"></div>

  <h1 class="title"><span class="accent">HIPAA</span> COMPLIANCE<br>OFFICER COURSE WITH<br>CERTIFICATE</h1>

  <div class="event-date">August 25th, 9:30am to 3pm<span class="lunch">(Lunch Included!)</span></div>
  <p class="venue">Harborview Conference Hotel at Palm Court<br>4820 Palm Court Avenue Fort Myers, Fl 33907</p>

  <svg class="photo-frame" viewBox="0 0 340 250" role="img" aria-label="Photo of seminar attendees taking notes at a conference table">
    <defs>
      <linearGradient id="scene" x1="0" y1="0" x2="1" y2="1">
        <stop offset="0" stop-color="#c9c3bb"/>
        <stop offset="0.5" stop-color="#8a6a52"/>
        <stop offset="1" stop-color="#4a3426"/>
      </linearGradient>
    </defs>
    <circle cx="125" cy="125" r="125" fill="var(--sky)"/>
    <circle cx="213" cy="125" r="124" fill="url(#scene)"/>
  </svg>

  <p class="price">Normally $299,<br>register now for only $49!</p>
  <p class="register-label">Register now at:</p>
  <p class="register-url">http://regpage.com/x7h2q</p>

  <section class="session" style="top:502px">
    <div class="session-label">
      <div class="session-title">HIPAA Topics</div>
      <p class="presented">PRESENTED BY</p>
      <p class="presenter">DANIEL HARGROVE,</p>
      <div class="partner-mark"><span class="dot"></span>Brightline Compliance</div>
      <p class="partner-name">Brightline Compliance Group</p>
    </div>
    <ul class="topics col-a">
      <li>Patient Access Guidance</li>
      <li>What you can charge for medical records.</li>
      <li>What is an Information Blocking?</li>
      <li>How to respond legally to subpoenas.</li>
      <li>The dangers of social media.</li>
    </ul>
    <ul class="topics col-b">
      <li>Why do I have to have my business associate agreement updated?</li>
      <li>Why your current policies could cause a penalty for Medicare Fraud.</li>
      <li>What you should know about current OCR enforcement actions. (Actual cases and enforcement letters.)</li>
    </ul>
  </section>

  <section class="session" style="top:656px">
    <div class="session-label">
      <div class="session-title">Cyber-Security Review</div>
      <p class="presented">PRESENTED BY</p>
      <p class="presenter">LAURA KESSLER</p>
      <div class="partner-mark"><span class="dot"></span>Northpoint</div>
      <p class="partner-name">Northpoint Health IT</p>
    </div>
    <ul class="topics col-a">
      <li>“How to avoid the $99 million dollar class action lawsuit”</li>
      <li>Lessons from recent cybersecurity incidents (Actual cases)</li>
      <li>New US Treasury Department sanctions and fines</li>
    </ul>
    <ul class="topics col-b">
      <li>Questions that you MUST ask your IT provider</li>
      <li>What to expect WHEN (not if) you have a cybersecurity event</li>
    </ul>
  </section>

  <section class="session" style="top:810px">
    <div class="session-label">
      <div class="session-title">Cyber Insurance</div>
      <p class="presented">PRESENTED BY</p>
      <p class="presenter">OWEN CASTILLO</p>
      <div class="partner-mark" style="margin-top:6px"><span class="dot"></span>Bayshore Risk Partners</div>
      <p class="partner-name">Bayshore Risk Partners</p>
    </div>
    <ul class="topics col-a">
      <li>The changing landscape of Cyber Insurance</li>
      <li>“I had a breach, when should I contact my insurance agent?”</li>
    </ul>
    <ul class="topics col-b">
      <li>What does Cyber Liability cover?</li>
    </ul>
  </section>

  <section class="kit-band">
    <h2 class="kit-title">Includes a FREE Information Blocking Kit!</h2>
    <p class="kit-sub">Full Compliance Kit for Information Blocking that includes:</p>
    <div class="kit-items">
      <div class="kit-item" style="left:39px;top:0">
        <svg width="40" height="40" viewBox="0 0 24 24" fill="none" stroke="#fff" stroke-width="1.6" stroke-linecap="round" stroke-linejoin="round"><path d="M20 13v6a2 2 0 0 1-2 2H5a2 2 0 0 1-2-2V6a2 2 0 0 1 2-2h6"/><path d="M17.5 2.5a2.1 2.1 0 0 1 3 3L12 14l-4 1 1-4z"/></svg>
        Updated for Information Blocking Business Associate Agreement.
      </div>
      <div class="kit-item" style="left:252px;top:0">
        <svg width="40" height="40" viewBox="0 0 24 24" fill="none" stroke="#fff" stroke-width="1.6" stroke-linecap="round" stroke-linejoin="round"><circle cx="9" cy="7" r="4"/><path d="M2 21v-1a6 6 0 0 1 6-6h2a6 6 0 0 1 6 6v1"/><path d="M16 3.2a4 4 0 0 1 0 7.6"/><path d="M22 21v-1a6 6 0 0 0-4-5.6"/></svg>
        Training on how to implement Information Blocking in your practice.
      </div>
      <div class="kit-item" style="left:469px;top:0">
        <svg width="40" height="40" viewBox="0 0 24 24" fill="none" stroke="#fff" stroke-width="1.6" stroke-linecap="round" stroke-linejoin="round"><rect x="3" y="3" width="18" height="18" rx="3"/><path d="M8 12l3 3 5-6"/></svg>
        Getting Started Guide and FACT Sheet.
      </div>
      <div class="kit-item" style="left:674px;top:0">
        <svg width="40" height="40" viewBox="0 0 24 24" fill="none" stroke="#fff" stroke-width="1.6" stroke-linecap="round" stroke-linejoin="round"><path d="M2 12s3.5-7 10-7 10 7 10 7-3.5 7-10 7S2 12 2 12z"/><circle cx="12" cy="12" r="3"/><path d="M3 21L21 3"/></svg>
        Forms to document exceptions and other Information Blocking requirements.
      </div>
    </div>
  </section>

  <div class="badge">Hard Copy &amp;<br>Digital Copy</div>
</div>
</body>
</html>
```